Stationary for Keeping Steady

we are in the process of creating a more professional image for our company Keeping Steady Paramedical Services. We have recently had a new logo and general brochure designed using artpitchhub and have been impressed by the quality of submissions.

We need:
- Letterhead (A4)
- Business Cards
- With compliments slips
- Email stationary

Letterhead information:
Address - 47 Wattlebrook Drive, Fernhollow Vic 3091
Phone - 1800 462 817
email - enquiries@keepsteady.com.au
Internet - www.keepsteady.com.au
ABN - 82 463 915 207
ACN - 264 871 035

Files need to be able to be edited in Illustrator CS2

Business Cards / with compliments slips / email stationary:
Double sided.
One side to have Name, Mobile number, company phone 1800462817, email, internet address

Files need to be able to be edited in Illustrator CS2 (except email stationary)

Our website is www.keepsteady.com.au for more information. Do not base designs on the website as it will eventually be revised.

Target Market(s)

Australian based businesses, government departments and schools. We specialise in corporate customers rather than public first aid course

Industry/Entity Type

Internet

Requirements
Must have
• Where applicable file to be editable in illustrator CS2 to allow future alterations.

```html
<!DOCTYPE html>
<html lang="en">
<head>
<meta charset="utf-8">
<title>Keeping Steady Paramedical Services – Business Card</title>
<link rel="stylesheet" href="https://fonts.googleapis.com/css2?family=Questrial&family=Montserrat:wght@600;700&display=swap">
<style>
  :root {
    --backdrop: #a3a4a8;
    --card: #ffffff;
    --brand-red: #c8322e;
    --ink: #111111;
    --muted: #7a7a7a;
    --rule: #8c8c8c;
  }
  html, body {
    margin: 0;
    padding: 0;
    width: 1200px;
    height: 900px;
    overflow: hidden;
    background: var(--backdrop);
  }
  .canvas {
    position: relative;
    width: 1200px;
    height: 900px;
  }
  .card {
    position: absolute;
    top: 177px;
    width: 524px;
    height: 319px;
    background: var(--card);
    box-shadow: 2px 3px 4px rgba(0, 0, 0, 0.35);
  }
  .card--front { left: 50px; }
  .card--back { left: 637px; }

  .brand {
    position: absolute;
    display: flex;
    align-items: center;
    color: var(--brand-red);
    font-family: "Questrial", sans-serif;
    white-space: nowrap;
  }
  .brand__mark {
    display: block;
    background: var(--brand-red);
  }
  .card--front .brand {
    left: 33px;
    top: 110px;
    gap: 26px;
    font-size: 44px;
  }
  .card--front .brand__mark { width: 86px; height: 86px; }

  .card--back .brand {
    left: 28px;
    top: 226px;
    gap: 12px;
    font-size: 22px;
  }
  .card--back .brand__mark { width: 40px; height: 40px; }

  .person {
    position: absolute;
    left: 29px;
    top: 26px;
    font-family: "Questrial", sans-serif;
    color: var(--ink);
  }
  .person__name {
    margin: 0 0 12px;
    font-family: "Montserrat", sans-serif;
    font-weight: 700;
    font-size: 23px;
    text-decoration: underline;
    text-underline-offset: 4px;
    text-decoration-thickness: 1.5px;
  }
  .contact {
    margin: 0;
    font-size: 18px;
    line-height: 22.5px;
  }
  .contact__label {
    font-family: "Montserrat", sans-serif;
    font-weight: 600;
  }
  .divider {
    position: absolute;
    left: 29px;
    right: 29px;
    top: 212px;
    border: 0;
    border-top: 1px solid var(--rule);
    margin: 0;
  }
  .address {
    position: absolute;
    left: 295px;
    top: 236px;
    margin: 0;
    font-family: "Questrial", sans-serif;
    font-style: normal;
    font-size: 16px;
    line-height: 19px;
    color: var(--muted);
  }
</style>
</head>
<body>
<main class="canvas">
  <section class="card card--front" aria-label="Business card front">
    <div class="brand">
      <span class="brand__mark" aria-hidden="true"></span>
      <span class="brand__name">Keeping Steady</span>
    </div>
  </section>

  <section class="card card--back" aria-label="Business card back">
    <div class="person">
      <h1 class="person__name">Callum Ashbury</h1>
      <p class="contact">
        <span class="contact__label">Mobile</span> 0400 000 000<br>
        <span class="contact__label">Phone</span> 1800 462 817<br>
        callum@keepsteady.com.au
      </p>
    </div>
    <hr class="divider">
    <div class="brand">
      <span class="brand__mark" aria-hidden="true"></span>
      <span class="brand__name">Keeping Steady</span>
    </div>
    <address class="address">
      47 Wattlebrook Drive<br>
      Fernhollow VIC 3091<br>
      www.keepsteady.com.au
    </address>
  </section>
</main>
</body>
</html>
```